Event flyer for Sunday night Youth Group

Need a 4 x 6 or 5 x 7 flyer for a new youth group starting on April 14. The youth group is for students in middle school and high school so it needs to look fun and cool, but not childish. I prefer it not to include pictures of people unless it's so obscure you can't really see their faces. I've uploaded some pictures of flyers I like. I've also attached a couple versions of our logo to use on the flyer.
Information the flyer needs to include:
Youth Group
Sundays, 6-8pm (beginning April 14)
Location: Merriwick's - 4219 Hollowfern Ln S, Alderbrook, 97418
There will be dinner, games, friends, and a message.
Target Market(s)
Youth ages 13-18
Industry/Entity Type
Church
Colors
Designer to choose colors to be used in the design.
Look and feel

```html
<!DOCTYPE html>
<html lang="en">
<head>
<meta charset="utf-8">
<title>Youth Group Flyer</title>
<link rel="stylesheet" href="https://fonts.googleapis.com/css2?family=Bebas+Neue&family=Montserrat:ital,wght@0,400;0,500;0,600;0,800;1,900&family=Mrs+Saint+Delafield&display=swap">
<style>
  :root {
    --page: #ffffff;
    --royal: #1f3fd6;
    --royal-deep: #0c1a8a;
    --navy: #081058;
    --glow: #5f86ff;
    --white: #ffffff;
    --ice: #c7d3ff;
    --silver: #e2e4ea;
    --band: #0d1f9e;
    --cyan: #3cc8ff;
  }
  * { margin: 0; padding: 0; box-sizing: border-box; }
  html, body { width: 889px; height: 1200px; overflow: hidden; background: var(--page); }
  .flyer {
    position: absolute; left: 77px; top: 48px; width: 737px; height: 1106px;
    overflow: hidden; color: var(--white);
    box-shadow: 0 14px 40px rgba(0,0,0,.45);
    background: var(--royal);
  }
  .backdrop {
    position: absolute; inset: 0;
    background:
      radial-gradient(ellipse 60% 40% at 50% 52%, rgba(95,134,255,.55), transparent 70%),
      radial-gradient(ellipse 80% 30% at 50% 95%, rgba(120,150,255,.45), transparent 70%),
      repeating-linear-gradient(90deg, rgba(8,16,88,.45) 0 40px, rgba(40,70,220,.2) 40px 90px),
      linear-gradient(180deg, var(--royal-deep) 0%, var(--royal) 45%, #2a4ce0 75%, #3a5cf0 100%);
  }
  .stage-ring {
    position: absolute; left: 114px; top: 314px; width: 518px; height: 518px; border-radius: 50%;
    background: radial-gradient(circle, #1a2fb0 0%, #0e1c8a 62%, #2b4be6 66%, #11208f 72%, transparent 74%);
    box-shadow: 0 0 30px rgba(95,134,255,.6);
  }
  .grade-tag {
    position: absolute; top: 32px; font-family: "Bebas Neue", sans-serif;
    font-size: 27px; line-height: 30px; letter-spacing: 4px;
  }
  .grade-tag.left { left: 31px; }
  .grade-tag.right { right: 29px; text-align: right; }
  .church-name {
    position: absolute; left: 0; right: 0; top: 208px; text-align: center;
    font-family: "Montserrat", sans-serif; color: var(--white);
  }
  .church-name .main { display: block; font-weight: 600; font-size: 52px; line-height: 56px; letter-spacing: 1px; }
  .church-name .sub { display: block; font-weight: 600; font-size: 27px; line-height: 34px; letter-spacing: 11px; margin-top: 2px; padding-left: 11px; }
  .invite {
    position: absolute; left: 0; right: 0; top: 362px; text-align: center;
    font-family: "Mrs Saint Delafield", cursive; font-size: 96px; line-height: 100px;
    transform: rotate(-6deg); text-shadow: 0 0 10px rgba(8,16,88,.8);
  }
  .headline {
    position: absolute; left: 0; right: 0; top: 462px; text-align: center;
    font-family: "Montserrat", sans-serif; font-weight: 900; font-style: italic;
    font-size: 130px; line-height: 110px; letter-spacing: -5px;
    color: var(--silver);
    text-shadow: 0 3px 0 #9aa0b5, 0 6px 0 #6a7090, 0 0 24px rgba(180,200,255,.7);
  }
  .when {
    position: absolute; left: 0; right: 0; top: 850px;
    display: flex; justify-content: center; align-items: stretch;
    font-family: "Bebas Neue", sans-serif;
  }
  .when .date { text-align: center; padding-right: 16px; border-right: 2px solid var(--white); }
  .when .day-num { display: block; font-size: 126px; line-height: 100px; }
  .when .month { display: block; font-size: 36px; line-height: 30px; color: var(--ice); }
  .when .time-block { padding-left: 16px; }
  .when .day { display: block; font-size: 70px; line-height: 62px; color: var(--ice); }
  .when .hours { display: block; font-size: 88px; line-height: 70px; }
  .activities {
    position: absolute; left: 0; right: 0; top: 999px; height: 46px;
    background: linear-gradient(90deg, rgba(13,31,158,.5), var(--band) 20%, var(--band) 80%, rgba(13,31,158,.5));
    border-top: 2px solid var(--cyan); border-bottom: 2px solid var(--cyan);
    display: flex; align-items: center; justify-content: center;
    font-family: "Montserrat", sans-serif; font-weight: 800; font-size: 26px; letter-spacing: 2px; color: var(--ice);
  }
  .location {
    position: absolute; left: 0; right: 0; top: 1062px;
    display: flex; align-items: center; justify-content: center; gap: 9px;
    font-family: "Montserrat", sans-serif; font-weight: 500; font-size: 19px;
  }
  .location svg { width: 20px; height: 26px; }
</style>
</head>
<body>
  <main class="flyer">
    <div class="backdrop" role="img" aria-label="Blue-lit concert stage with speaker stacks, light beams and a crowd in silhouette"></div>
    <div class="stage-ring" role="img" aria-label="Glowing circular stage frame ringed with bulbs"></div>

    <p class="grade-tag left">Middle<br>School</p>
    <p class="grade-tag right">High<br>School</p>

    <h2 class="church-name"><span class="main">BRIGHTPATH</span><span class="sub">FELLOWSHIP</span></h2>

    <p class="invite">You are Invited</p>
    <h1 class="headline">YOUTH<br>GROUP</h1>

    <div class="when">
      <div class="date"><span class="day-num">14</span><span class="month">April</span></div>
      <div class="time-block"><span class="day">Sunday</span><span class="hours">6-8PM</span></div>
    </div>

    <p class="activities">DINNER · GAMES · FRIENDS · A MESSAGE</p>

    <p class="location">
      <svg viewBox="0 0 20 26" aria-hidden="true"><path d="M10 0C4.5 0 0 4.4 0 9.8 0 17 10 26 10 26s10-9 10-16.2C20 4.4 15.5 0 10 0z" fill="#fff"/><circle cx="10" cy="9.8" r="3.6" fill="#1f3fd6"/></svg>
      MERRIWICK'S – 4219 HOLLOWFERN LN S, ALDERBROOK, 97418
    </p>
  </main>
</body>
</html>
```